Brightwell Giving Inc

We need a full re-design of our non-profit organization website (www.brightwellgiving.org). Ideally, we are looking to make it more attractive, user-friendly, and interactive with our business model.

Please make sure to user colors that ago with our logo.

We need a homepage done and we also need a content page done where we will use for the other pages to fill with content.

Target Market(s)

Clothes/textiles donations.

Industry/Entity Type

Charity

Number of Pages Required

2 page

Colors

Designer to choose colors to be used in the design.

Requirements
Must have
• It must match the styling of our logo and same colors as current website. (www.brightwellgiving.org)
Nice to have
• Sleek homepage that is easy to understand and get our main points across.

```html
<!DOCTYPE html>
<html lang="en">
<head>
<meta charset="utf-8">
<title>Brightwell Giving – Think Globally while Donating Locally</title>
<link rel="stylesheet" href="https://fonts.googleapis.com/css2?family=Lato:wght@400;700;900&display=swap">
<style>
:root{
  --green:#3f6b22;
  --green-dark:#355c1c;
  --mint:#c8eab4;
  --yellow:#f7c600;
  --ink:#2b2b2b;
  --text:#3a3a3a;
  --muted:#6b6b6b;
  --footer:#ebebeb;
  --line:#9a9a9a;
  --white:#ffffff;
}
*{box-sizing:border-box;margin:0;padding:0}
html,body{width:1200px;height:2564px;overflow:hidden}
body{font-family:'Lato',Arial,sans-serif;color:var(--text);background:var(--white);position:relative}
.btn{display:inline-flex;align-items:center;justify-content:center;background:var(--green);color:var(--white);font-weight:700;font-size:16px;text-transform:uppercase;text-decoration:none;border-radius:2px;letter-spacing:.2px}
.btn--ghost{background:transparent;border:1.5px solid var(--white)}
.section-title{font-size:26px;font-weight:700;color:var(--ink);text-transform:uppercase;position:relative;padding-bottom:14px}
.section-title::after{content:"";position:absolute;left:0;bottom:0;width:52px;height:3px;background:var(--green)}
.section-title--center{text-align:center}
.section-title--center::after{left:50%;transform:translateX(-50%)}
.brand{display:flex;align-items:center;gap:10px;text-decoration:none}
.brand__mark{width:40px;height:40px;background:var(--green);border-radius:3px;flex:none}
.brand__name{font-size:20px;font-weight:900;color:var(--green);line-height:1;text-transform:uppercase;letter-spacing:.3px}
.social{display:flex;gap:10px;list-style:none}
.social li{width:38px;height:38px;border:1.5px solid var(--line);border-radius:50%;display:flex;align-items:center;justify-content:center;font-size:10px;color:var(--muted);font-weight:700}

/* header */
.site-header{position:absolute;left:0;top:0;width:1200px;height:111px}
.site-header .brand{position:absolute;left:89px;top:50px}
.site-header .social{position:absolute;left:670px;top:22px}
.site-header .btn{position:absolute;left:979px;top:19px;width:132px;height:43px}
.main-nav{position:absolute;right:89px;top:74px;display:flex;gap:22px;list-style:none}
.main-nav a{font-size:14.5px;color:var(--ink);text-decoration:none;text-transform:uppercase;font-weight:400;display:block;padding-bottom:13px;position:relative}
.main-nav a.is-active::after{content:"";position:absolute;left:0;right:0;bottom:0;height:3px;background:var(--green)}

/* hero */
.hero{position:absolute;left:0;top:111px;width:1200px;height:439px}
.hero__photo{position:absolute;inset:0;background:radial-gradient(ellipse at 48% 30%,#6b5a48 0%,#3a2e25 35%,#151210 70%,#0b0a09 100%)}
.hero__content{position:absolute;left:0;right:0;top:152px;text-align:center;color:var(--white)}
.hero__title{font-size:34px;font-weight:900;text-transform:uppercase;letter-spacing:.3px}
.hero__sub{font-size:20px;font-weight:700;margin-top:4px}
.hero__actions{display:flex;justify-content:center;gap:20px;margin-top:38px}
.hero__actions .btn{width:141px;height:43px}
.hero__dots{position:absolute;left:50%;top:411px;transform:translateX(-50%);display:flex;gap:6px}
.hero__dots span{width:11px;height:11px;border:1.5px solid var(--white);border-radius:50%}
.hero__dots span.is-active{background:var(--white)}

/* welcome */
.welcome{position:absolute;left:87px;top:630px;width:1024px;height:320px}
.welcome__text{position:absolute;left:0;top:68px;width:668px;font-size:15px;line-height:25.3px;color:var(--text)}
.welcome__photo{position:absolute;left:699px;top:72px;width:325px;height:197px;background:radial-gradient(ellipse at 50% 55%,#5fae3a 0%,#3f8a2a 50%,#2c5e22 100%)}
.welcome .btn{position:absolute;left:0;top:254px;width:140px;height:44px}

/* work & news */
.work-news{position:absolute;left:0;top:1017px;width:1200px;height:560px;background:var(--mint)}
.work-news .section-title{font-size:22px;padding-bottom:12px}
.work{position:absolute;left:87px;top:24px;width:523px}
.work__map{margin-top:20px;width:521px;height:393px;background:linear-gradient(160deg,#c9dcb0 0%,#e8e4d2 45%,#d6dfc4 75%,#a9c9e6 100%)}
.work .btn{position:absolute;left:154px;top:468px;width:212px;height:43px}
.news{position:absolute;left:675px;top:24px;width:436px}
.news__list{list-style:none;margin-top:24px;width:410px}
.news__list li{position:relative;padding-left:28px;font-size:16px;font-weight:700;color:#4d4d4d;line-height:27px;margin-bottom:12px}
.news__list li::before{content:"";position:absolute;left:2px;top:50%;margin-top:-7px;border-left:7px solid var(--green);border-top:7px solid transparent;border-bottom:7px solid transparent}
.news .btn{position:absolute;left:113px;top:468px;width:210px;height:43px}

/* mission */
.mission{position:absolute;left:0;top:1577px;width:1200px;height:363px;text-align:center}
.mission .section-title{margin-top:84px;display:inline-block}
.mission__text{width:1010px;margin:26px auto 0;font-size:15px;line-height:26.5px;color:var(--text)}
.mission__text strong{color:var(--ink)}

/* support */
.support{position:absolute;left:0;top:1940px;width:1200px;height:312px;background:var(--yellow);text-align:center}
.support__title{font-size:34px;font-weight:900;color:var(--ink);text-transform:uppercase;margin-top:30px}
.support__text{width:1000px;margin:18px auto 0;font-size:15px;font-weight:700;line-height:26px;color:#3a3420}
.support .btn{margin-top:46px;width:140px;height:44px}

/* footer */
.site-footer{position:absolute;left:0;top:2252px;width:1200px;height:312px;background:var(--footer);border-top:3px solid #7aa25a}
.site-footer .brand{position:absolute;left:176px;top:26px}
.footer-nav{position:absolute;left:174px;top:106px;display:grid;grid-template-columns:175px 160px;row-gap:13px;list-style:none}
.footer-nav a{font-size:14.5px;color:var(--ink);text-decoration:none;text-transform:uppercase}
.footer-heading{font-size:22px;font-weight:700;color:var(--ink);text-transform:uppercase}
.join{position:absolute;left:697px;top:36px}
.signup{display:flex;margin-top:16px;width:325px;height:53px}
.signup__icon{width:54px;background:var(--green);display:flex;align-items:center;justify-content:center}
.signup__field{flex:1;background:#c4c4c4;display:flex;align-items:center;padding-left:16px;font-size:15px;color:#6f8f55}
.connect{position:absolute;left:697px;top:160px}
.connect .social{margin-top:12px;gap:11px}
.copyright{position:absolute;left:0;right:0;top:278px;text-align:center;font-size:13px;color:var(--muted);text-transform:uppercase;letter-spacing:.3px}
</style>
</head>
<body>

<header class="site-header">
  <a class="brand" href="#"><span class="brand__mark"></span><span class="brand__name">Brightwell Giving</span></a>
  <ul class="social">
    <li>Share</li><li>Chirp</li><li>Snap</li><li>Plus</li><li>Work</li><li>Pins</li>
  </ul>
  <a class="btn" href="#">Donate</a>
  <ul class="main-nav">
    <li><a class="is-active" href="#">Home</a></li>
    <li><a href="#">Missions</a></li>
    <li><a href="#">Family</a></li>
    <li><a href="#">How it works</a></li>
    <li><a href="#">News</a></li>
    <li><a href="#">About us</a></li>
    <li><a href="#">Wall of needs</a></li>
  </ul>
</header>

<section class="hero">
  <div class="hero__photo" role="img" aria-label="Close-up photo of a hand pulling folded dollar bills from a leather wallet"></div>
  <div class="hero__content">
    <h1 class="hero__title">Think Globally While Donating Locally</h1>
    <p class="hero__sub">Think Globally while Donating Locally Globally while Donating</p>
    <div class="hero__actions">
      <a class="btn btn--ghost" href="#">About us</a>
      <a class="btn" href="#">Donate now</a>
    </div>
  </div>
  <div class="hero__dots"><span class="is-active"></span><span></span><span></span></div>
</section>

<section class="welcome">
  <h2 class="section-title">Welcome</h2>
  <p class="welcome__text">Brightwell Giving is a non-profit organization that was created for one purpose: helping the less fortunate in our country's time of greatest need. Started in 2007, Brightwell Giving has been a dedicated member of its local communities over the past four years. The company's clothing collection efforts have allowed it to provide some of the neediest members of the community to clothe themselves and their families. The company's goal is to ensure that some of the most basic needs of the community's members are met thru the philanthropic efforts of the organizations members and contributors.</p>
  <div class="welcome__photo" role="img" aria-label="Photo of a group of people holding hands in a large circle on a green lawn"></div>
  <a class="btn" href="#">Learn more</a>
</section>

<section class="work-news">
  <div class="work">
    <h2 class="section-title">Where we work</h2>
    <div class="work__map" role="img" aria-label="Map of the northeastern region marking the clothing donation bin locations"></div>
    <a class="btn" href="#">See where we work</a>
  </div>
  <div class="news">
    <h2 class="section-title">Latest news</h2>
    <ul class="news__list">
      <li>Brightwell Giving created the flyer for inform the people in Manhattan to help others by giving donation.</li>
      <li>We are starting the charity projects to collect funds on FundCircle</li>
      <li>CHARITY PROJECT HELPING HANDS-WINTER DRIVE</li>
      <li>Charity Project HELPING HANDS donation boxes</li>
      <li>Brightwell Giving BidMarket store</li>
      <li>Brightwell Giving Street Sales</li>
      <li>Opened Thrift Store in Oct</li>
    </ul>
    <a class="btn" href="#">See all news</a>
  </div>
</section>

<section class="mission">
  <h2 class="section-title section-title--center">Our Mission</h2>
  <p class="mission__text"><strong>Brightwell Giving</strong> has a two part mission to <strong>help local communities while helping the planet</strong>. The average American discards 68 lbs of clothing annually. <strong>That is 1,325,340,196 lbs for New York State alone and 21,202,400,000 lbs for the U.S. every year!</strong> By keeping unwanted clothes out of the trash can we are greatly reducing the amount of material that enters our landfills. We are also turning the unwanted clothes into funding for our local communities. We are asking for your help to increase local support. Simply put, <strong>there is no better time to act than now.</strong></p>
</section>

<section class="support">
  <h2 class="support__title">Support us</h2>
  <p class="support__text">Vivamus nec aliquet odio. Nunc malesuada eu tellus quis aliquet. Morbi turpis erat, cursus sed magna a, euismod dictum sapien. Nulla eu consectetur quam, at pulvinar lorem.</p>
  <a class="btn" href="#">Donate now</a>
</section>

<footer class="site-footer">
  <a class="brand" href="#"><span class="brand__mark"></span><span class="brand__name">Brightwell Giving</span></a>
  <ul class="footer-nav">
    <li><a href="#">Home</a></li><li><a href="#">News</a></li>
    <li><a href="#">Missions</a></li><li><a href="#">About us</a></li>
    <li><a href="#">Family</a></li><li><a href="#">Wall of needs</a></li>
    <li><a href="#">How it works</a></li><li><a href="#">Contact</a></li>
  </ul>
  <div class="join">
    <h3 class="footer-heading">Join our community</h3>
    <div class="signup">
      <span class="signup__icon">
        <svg width="28" height="20" viewBox="0 0 28 20" fill="none" stroke="#ffffff" stroke-width="2"><rect x="1" y="1" width="26" height="18"/><path d="M1 1l13 10L27 1"/></svg>
      </span>
      <span class="signup__field">Sign Up For Updates</span>
    </div>
  </div>
  <div class="connect">
    <h3 class="footer-heading">Connect with us</h3>
    <ul class="social">
      <li>Share</li><li>Chirp</li><li>Snap</li><li>Plus</li><li>Work</li><li>Pins</li>
    </ul>
  </div>
  <p class="copyright">© 2018 Brightwell Giving Inc.</p>
</footer>

</body>
</html>
```